Pelican Crest landing page design

We need a landing page designed for an ecommerce website that sales fresh US domestic shrimp from the Gulf of Mexico and ships them direct to the consumer "From Our Shore To Your Door". For the landing page, we would like customers to be able to place an order and or inquire further about our product as well as links to social media. The company logo is attached

1 page

```html
<!DOCTYPE html>
<html lang="en">
<head>
<meta charset="utf-8">
<title>Pelican Crest — Fresh Gulf Shrimp</title>
<link rel="stylesheet" href="https://fonts.googleapis.com/css2?family=Montserrat:wght@400;500;600;700&display=swap">
<style>
:root{
  --orange:#ed884b;
  --orange-dark:#d2733d;
  --blue:#5bb8e6;
  --star:#6cc56e;
  --ink:#4a4a4a;
  --muted:#6b6b6b;
  --white:#ffffff;
}
*{box-sizing:border-box;margin:0;padding:0}
html,body{width:916px;height:1200px;overflow:hidden;background:var(--white)}
body{position:relative;font-family:"Montserrat",sans-serif;color:var(--ink)}
.abs{position:absolute}
a{color:inherit;text-decoration:none}

/* header */
.site-header{position:absolute;left:0;top:0;width:916px;height:48px;background:var(--white)}
.brand{position:absolute;left:177px;top:6px;display:flex;align-items:center;gap:5px}
.brand-mark{width:36px;height:36px;border-radius:50%;border:1.5px solid #9aa3ad}
.brand-name{font-size:11px;font-weight:600;letter-spacing:1.2px;color:#5a6470;text-transform:uppercase}
.main-nav a{position:absolute;top:18px;font-size:10px;color:var(--muted)}
.main-nav .is-active{color:var(--ink);border-bottom:1px solid var(--ink);padding:0 3px 3px}
.cart-icon{position:absolute;left:656px;top:17px}
.btn-signup{position:absolute;left:682px;top:14px;width:59px;height:20px;border:1.5px solid var(--orange);border-radius:3px;color:var(--orange);font-size:8px;font-weight:500;letter-spacing:.6px;display:flex;align-items:center;justify-content:center}

/* hero */
.hero{position:absolute;left:0;top:48px;width:916px;height:334px;
  background:radial-gradient(ellipse at 50% 60%,#d98a55 0%,#a3653b 30%,#6b4a2b 60%,#c9a53b 100%)}
.hero-title{position:absolute;left:0;top:124px;width:916px;text-align:center;font-size:21px;font-weight:700;color:var(--white);letter-spacing:.5px;text-shadow:0 1px 3px rgba(0,0,0,.35)}
.hero-sub{position:absolute;left:0;top:151px;width:916px;text-align:center;font-size:9.5px;font-weight:600;color:var(--white);letter-spacing:.4px;text-shadow:0 1px 2px rgba(0,0,0,.4)}
.btn-blue{position:absolute;width:96px;height:24px;background:var(--blue);color:var(--white);font-size:8px;font-weight:500;letter-spacing:.6px;display:flex;align-items:center;justify-content:center;border-radius:1px}

/* how it works */
.section-title{position:absolute;left:0;width:916px;text-align:center;font-size:14px;font-weight:700;letter-spacing:.8px;color:var(--ink)}
.step{position:absolute;width:180px;text-align:center}
.step-circle{width:77px;height:77px;margin:0 auto;border:1.6px solid var(--orange);border-radius:50%;display:flex;align-items:center;justify-content:center}
.step-title{margin-top:8px;font-size:13.5px;font-weight:500;color:var(--ink);letter-spacing:.3px}
.step-text{margin-top:3px;font-size:8.5px;color:var(--muted)}
.step-arrow{position:absolute;top:472px}

/* why */
.why-photo{position:absolute;left:0;top:622px;width:458px;height:258px;
  background:radial-gradient(ellipse at 55% 55%,#f19a73 0%,#c86f4f 35%,#5c6e3a 70%,#3c2f35 100%)}
.why-panel{position:absolute;left:458px;top:622px;width:458px;height:258px;background:var(--orange);color:var(--white);padding:20px 14px 0 13px}
.why-title{font-size:13.5px;font-weight:700;letter-spacing:.5px}
.why-panel p{margin-top:11px;font-size:8.3px;line-height:11.5px;width:270px}
.why-panel p:first-of-type{margin-top:18px}

/* reviews */
.review{position:absolute;top:936px;width:122px;text-align:center}
.review-stars{display:flex;justify-content:center;gap:2px}
.review-text{margin-top:4px;font-size:8.3px;line-height:9.2px;color:var(--muted)}
.review-name{margin-top:4px;font-size:8px;font-weight:600;color:var(--ink)}
.carousel-arrow{position:absolute;top:964px;font-size:16px;color:var(--muted)}
.more-reviews{position:absolute;left:0;top:1024px;width:916px;text-align:center;font-size:8.3px;color:var(--ink)}
.more-reviews span{color:var(--blue);font-size:6px}

/* footer */
.site-footer{position:absolute;left:0;top:1057px;width:916px;height:119px;background:var(--orange);color:var(--white)}
.footer-links a{position:absolute;left:214px;font-size:8.3px}
.footer-heading{position:absolute;font-size:9px;font-weight:600}
.social{position:absolute;top:1097px;width:38px;height:38px;border-radius:50%;background:var(--white)}
.contact-text{position:absolute;left:634px;top:1096px;width:68px;font-size:8.3px;line-height:9.2px;color:var(--white)}
.footer-bar{position:absolute;left:0;top:1176px;width:916px;height:24px;background:var(--orange-dark);color:var(--white);font-size:7px}
</style>
</head>
<body>

<header class="site-header">
  <div class="brand"><span class="brand-mark"></span><span class="brand-name">Pelican Crest</span></div>
  <nav class="main-nav">
    <a class="is-active" style="left:365px">Home</a>
    <a style="left:414px">How It Works</a>
    <a style="left:494px">Menu</a>
    <a style="left:538px">About</a>
  </nav>
  <svg class="cart-icon" width="14" height="13" viewBox="0 0 14 13" fill="none" stroke="#9a9a9a" stroke-width="1">
    <path d="M1 1h2l2 7h7l1.5-5H4"/><circle cx="6" cy="11" r="1"/><circle cx="11" cy="11" r="1"/>
  </svg>
  <a class="btn-signup">SIGN UP</a>
</header>

<section class="hero" role="img" aria-label="Grilled shrimp with dill and vegetables on a plate">
  <h1 class="hero-title">From our shore to your door</h1>
  <p class="hero-sub">Fresh Shrimp delivered directly at your doorstep.</p>
  <a class="btn-blue" style="left:410px;top:180px">GET STARTED</a>
</section>

<h2 class="section-title" style="top:402px">HOW IT WORKS</h2>

<div class="step" style="left:164px;top:438px">
  <div class="step-circle">
    <svg width="40" height="32" viewBox="0 0 40 32" fill="none" stroke="var(--orange)" stroke-width="1.2">
      <rect x="6" y="3" width="28" height="20" rx="1"/><path d="M2 26h36l-2 3H4z"/>
      <path d="M13 8h2l2 8h9l2-6H16"/><circle cx="18" cy="19" r="1"/><circle cx="25" cy="19" r="1"/>
    </svg>
  </div>
  <div class="step-title">Choose the order</div>
  <div class="step-text">Lorem ipsum dolor sit amet</div>
</div>
<svg class="step-arrow" style="left:322px" width="72" height="10" viewBox="0 0 72 10" fill="none" stroke="var(--blue)" stroke-width="1.3">
  <path d="M0 5h64" stroke-dasharray="5 4"/><path d="M62 1l8 4-8 4z" fill="var(--blue)"/>
</svg>
<div class="step" style="left:365px;top:438px">
  <div class="step-circle">
    <svg width="44" height="30" viewBox="0 0 44 30" fill="none" stroke="var(--orange)" stroke-width="1.2">
      <rect x="2" y="3" width="26" height="19"/><path d="M28 9h8l5 6v7H28z"/>
      <circle cx="10" cy="24" r="3"/><circle cx="34" cy="24" r="3"/>
      <circle cx="15" cy="12" r="5"/><path d="M13 9v6h2a3 3 0 0 0 0-6z"/>
    </svg>
  </div>
  <div class="step-title">We deliver</div>
  <div class="step-text">Lorem ipsum dolor sit amet</div>
</div>
<svg class="step-arrow" style="left:526px" width="72" height="10" viewBox="0 0 72 10" fill="none" stroke="var(--blue)" stroke-width="1.3">
  <path d="M0 5h64" stroke-dasharray="5 4"/><path d="M62 1l8 4-8 4z" fill="var(--blue)"/>
</svg>
<div class="step" style="left:572px;top:438px">
  <div class="step-circle">
    <svg width="36" height="32" viewBox="0 0 36 32" fill="none" stroke="var(--orange)" stroke-width="1.2">
      <path d="M8 18a12 12 0 0 1 24 0z"/><path d="M6 18h28"/><circle cx="20" cy="5" r="1.5"/>
      <path d="M2 22h4v8H2z"/><path d="M6 23h8l6 2h6l-2 3H6"/>
    </svg>
  </div>
  <div class="step-title">You enjoy</div>
  <div class="step-text">Lorem ipsum dolor sit amet</div>
</div>

<a class="btn-blue" style="left:410px;top:575px">LEARN MORE</a>

<div class="why-photo" role="img" aria-label="Bowl of fresh salad topped with cooked shrimp"></div>
<section class="why-panel">
  <h2 class="why-title">WHY YOU WILL LOVE OUR SHRIMPS</h2>
  <p>Lorem ipsum dolor sit amet, consectetur adipiscing elit. Suspendisse mollis sit amet ligula vit ae commodo.</p>
  <p>Pellentesque habitant morbi tristique senectus et netus et malesuada fames ac turpis egestas. Ut viverra consequat venenatis. Vestibulum scelerisque, lacus a pulvinar condimentum, nisi orci luctus dui, at molestie libero quam sit amet enim. Vivamus dictum venenatis tincidunt.</p>
  <p>Morbi viverra arcu ac quam pharetra egestas. Sed consequat lacus sed mauris fermentum ultricies. Pellentesque id neque magna. Ut et mi sed sem maximus rhoncus id eu arcu. Vestibulum volutpat elit sapien, ut cursus massa congue laoreet.</p>
  <p>Pellentesque habitant morbi tristique senectus et netus et malesuada fames ac turpis egestas.</p>
</section>

<h2 class="section-title" style="top:901px">WHAT OUR CUSTOMERS ARE SAYING</h2>

<svg width="0" height="0" style="position:absolute">
  <defs><symbol id="star" viewBox="0 0 24 24"><path fill="var(--star)" d="M12 1.5l3.2 7 7.6.8-5.7 5.1 1.6 7.5L12 18l-6.7 3.9 1.6-7.5L1.2 9.3l7.6-.8z"/></symbol></defs>
</svg>

<span class="carousel-arrow" style="left:182px">&lt;</span>
<div class="review" style="left:212px">
  <div class="review-stars"><svg width="14" height="14"><use href="#star"/></svg><svg width="14" height="14"><use href="#star"/></svg><svg width="14" height="14"><use href="#star"/></svg><svg width="14" height="14"><use href="#star"/></svg><svg width="14" height="14"><use href="#star"/></svg></div>
  <p class="review-text">Lorem ipsum dolor sit amet, consectetur adipiscing elit, sed do eiusmod tempor incididunt ut labore et</p>
  <p class="review-name">Glen T</p>
</div>
<div class="review" style="left:396px">
  <div class="review-stars"><svg width="14" height="14"><use href="#star"/></svg><svg width="14" height="14"><use href="#star"/></svg><svg width="14" height="14"><use href="#star"/></svg><svg width="14" height="14"><use href="#star"/></svg><svg width="14" height="14"><use href="#star"/></svg></div>
  <p class="review-text">Lorem ipsum dolor sit amet, consectetur adipiscing elit, sed do eiusmod tempor incididunt ut labore et</p>
  <p class="review-name">Marisol</p>
</div>
<div class="review" style="left:581px">
  <div class="review-stars"><svg width="14" height="14"><use href="#star"/></svg><svg width="14" height="14"><use href="#star"/></svg><svg width="14" height="14"><use href="#star"/></svg><svg width="14" height="14"><use href="#star"/></svg><svg width="14" height="14"><use href="#star"/></svg></div>
  <p class="review-text">Lorem ipsum dolor sit amet, consectetur adipiscing elit, sed do eiusmod tempor incididunt ut labore et</p>
  <p class="review-name">Nadine</p>
</div>
<span class="carousel-arrow" style="left:723px">&gt;</span>

<a class="more-reviews">See more reviews <span>&#9654;</span></a>

<footer class="site-footer">
  <nav class="footer-links">
    <a style="top:24px">Home</a>
    <a style="top:39px">How it works</a>
    <a style="top:54px">Menu</a>
    <a style="top:69px">About</a>
  </nav>
  <div class="footer-heading" style="left:0;width:916px;text-align:center;top:23px">Follow our Social Media</div>
  <div class="footer-heading" style="left:634px;top:24px">Contact</div>
</footer>
<span class="social" style="left:377px" role="img" aria-label="Photo sharing profile"></span>
<span class="social" style="left:439px" role="img" aria-label="Social network page"></span>
<span class="social" style="left:501px" role="img" aria-label="Microblog profile"></span>
<p class="contact-text">Lorem ipsum dolor sit amet, consectetur adipiscing elit,</p>

<div class="footer-bar">
  <span class="abs" style="left:177px;top:8px">© 2019 Pelican Crest.</span>
  <span class="abs" style="left:685px;top:6px">Privacy</span>
  <span class="abs" style="left:719px;top:6px">Terms</span>
</div>

</body>
</html>
```